Annual Event PPT Template

We need a PowerPoint template to use for a big annual event we host. Attached is the logo we use for everything. You can also reference our website (listed below) and our letterhead for design inspiration.

Please be sure to include our contact information on all of the PPT slides:
1. Phone: 802-431-7296
2. Address: 342 Pebble Creek Road, Ashford Falls, VT 05677
3. Website: www.Corvalix.com

```html
<!DOCTYPE html>
<html lang="en">
<head>
<meta charset="utf-8">
<title>Corvalix – Presentation Deck</title>
<link rel="stylesheet" href="https://fonts.googleapis.com/css2?family=Montserrat:wght@400;500;800&family=Signika:wght@400;600;700&family=Open+Sans:wght@400;600;700&display=swap">
<style>
:root{
  --blue:#2f5d8c;
  --navy:#1f4169;
  --deep:#1b1f4a;
  --orange:#f7941d;
  --page:#e4e7ec;
  --mist:#eef1f5;
  --ink:#444a55;
  --muted:#8a93a0;
  --white:#fff;
}
*{box-sizing:border-box;margin:0;padding:0}
html,body{width:1200px;height:2444px;overflow:hidden}
body{background:var(--page);font-family:"Open Sans",sans-serif;color:var(--ink);position:relative}
.hero-photo{position:absolute;left:0;top:0;width:1200px;height:760px;
  background:linear-gradient(160deg,#b9c6d3 0%,#a9b3bb 35%,#c8c3b9 55%,#d8dce2 100%);
  clip-path:polygon(0 0,100% 0,100% 20%,0 100%);opacity:.85}
.hero-fade{position:absolute;left:0;top:0;width:1200px;height:760px;
  background:linear-gradient(90deg,rgba(228,231,236,0) 30%,rgba(228,231,236,.9) 70%)}
.brand{position:absolute;left:0;width:1200px;top:52px;text-align:center;font-family:"Signika",sans-serif;font-weight:700;font-size:54px;color:var(--blue);letter-spacing:-.5px}
.deck-title{position:absolute;left:70px;top:290px;font-family:"Montserrat",sans-serif;line-height:.98}
.deck-title .a{display:block;font-size:62px;font-weight:800;color:var(--blue)}
.deck-title .b{display:block;font-size:62px;font-weight:500;color:var(--deep);padding-left:126px}
.hero-slide{position:absolute;left:563px;top:193px;width:468px;height:262px;box-shadow:0 10px 30px rgba(30,50,80,.25)}
.section-rule{position:absolute;left:530px;top:642px;width:185px;height:1px;background:#9aa3ae}
.section-title{position:absolute;left:0;width:1200px;top:650px;text-align:center;font-family:"Montserrat",sans-serif;font-size:33px;color:var(--orange);font-weight:400}

.grid{position:absolute;left:36px;top:732px;display:grid;grid-template-columns:repeat(3,353px);grid-auto-rows:199px;column-gap:22px;row-gap:15px}
.slide{position:relative;background:var(--white);overflow:hidden;box-shadow:0 3px 12px rgba(40,60,100,.18);font-size:4.3px;line-height:1.45}
.slide.last{grid-column:2}
.swoosh::before,.swoosh::after{content:"";position:absolute;left:0;top:0;width:100%;height:30px}
.swoosh::before{background:var(--orange);clip-path:polygon(0 0,100% 0,100% 26px,80% 17px,55% 10px,25% 6px,0 5px)}
.swoosh::after{background:var(--navy);clip-path:polygon(0 0,100% 0,100% 22px,80% 13px,55% 7px,25% 3px,0 2px)}
.foot{position:absolute;left:0;right:0;bottom:0;height:13px;border-top:1px solid var(--orange);display:flex;align-items:center;gap:16px;padding:0 6px;font-size:4px;color:#555;white-space:nowrap}
.foot span{display:flex;align-items:center;gap:2px}
.foot .flogo{font-family:"Signika",sans-serif;font-weight:700;color:var(--blue);font-size:5px;margin-right:14px}
.foot .pg{margin-left:auto;background:var(--navy);color:#fff;font-weight:700;padding:0 3px;font-size:4px}
.ic{width:5px;height:5px;fill:var(--navy)}
.h{font-family:"Signika",sans-serif;font-weight:600;color:var(--blue);text-align:center}
.sub{font-size:4.5px;letter-spacing:1.6px;color:var(--muted);text-align:center;text-transform:uppercase}
.txt{color:#555;text-align:justify}
.abs{position:absolute}
.photo{position:absolute;background:linear-gradient(135deg,#9fb2c6,#6d86a2 60%,#4d6a8c)}
.photo-soft{position:absolute;background:linear-gradient(180deg,#dfe4ea,#f6f7f9)}
.logo{font-family:"Signika",sans-serif;font-weight:700;color:var(--blue)}

.title-top{position:absolute;left:0;top:0;right:0;height:68%;background:linear-gradient(135deg,#577da3,#2f5d8c 55%,#27507c)}
.title-top::after{content:"";position:absolute;left:0;right:0;bottom:0;height:2px;background:var(--orange)}
.title-main{position:absolute;left:0;right:0;top:36%;text-align:center;color:#fff;font-family:"Open Sans",sans-serif}
.title-main strong{display:block;font-weight:700;font-size:.058em}
.title-main em{display:block;font-style:normal;font-weight:700;letter-spacing:.16em;font-size:.02em}
.title-logo{position:absolute;left:0;right:0;text-align:center}
.title-foot{position:absolute;left:0;right:0;display:flex;justify-content:center;gap:30px;color:#555;white-space:nowrap}
.title-foot span{display:flex;align-items:center;gap:3px}

.agenda-list{position:absolute;left:215px;top:36px;list-style:none;font-size:4.6px;color:#666}
.agenda-list li{display:flex;gap:14px;margin-bottom:6.4px}
.agenda-list i{font-style:normal;width:8px;color:#999}

.pill{display:inline-block;background:var(--orange);color:#fff;border-radius:8px;padding:2px 16px;font-size:4px}
.numc{position:absolute;width:18px;height:18px;border-radius:50%;background:#fff;border:1.5px solid #dfe4ea;color:var(--navy);font-weight:700;font-size:5px;display:flex;align-items:center;justify-content:center}
.card{position:absolute;background:#fff;border-radius:3px;text-align:center;box-shadow:0 2px 5px rgba(0,0,0,.2)}
.card b{display:block;color:var(--navy);font-size:6px;font-weight:600;margin-top:8px}
.card small{font-size:3px;color:#888}
.ind{position:absolute;width:82px;height:44px;background:var(--blue);border-radius:6px;color:#fff;font-size:6px;font-weight:600;display:flex;align-items:center;justify-content:center;text-align:center;line-height:1.2;box-shadow:0 2px 4px rgba(0,0,0,.25)}
.ind::before{content:"";position:absolute;top:-7px;left:50%;margin-left:-7px;width:14px;height:14px;border-radius:50%;background:#fff;border:1.5px solid #cfd8e3}
.svc{position:absolute;right:14px;width:56px;text-align:center;font-size:4px;font-weight:600;color:var(--navy)}
.svc i{display:block;margin:0 auto 2px;width:26px;height:26px;border-radius:50%;background:var(--blue);border:2px solid #fff;box-shadow:0 0 0 1px #cfd8e3}
.bul{list-style:none;font-size:4px;letter-spacing:1px;color:var(--blue);text-transform:uppercase}
.bul li::before{content:"› ";color:var(--orange)}
.dot{position:absolute;width:16px;height:16px;border-radius:50%}
.chev{position:absolute;top:74px;width:66px;height:80px;color:#fff;text-align:center;clip-path:polygon(0 0,80% 0,100% 50%,80% 100%,0 100%,18% 50%)}
.chev b{display:block;font-size:4.5px;letter-spacing:1px;margin-top:6px;opacity:.8}
.chev strong{display:block;font-size:14px;font-weight:600;line-height:1}
.chev p{font-size:3.3px;padding:4px 14px 0 16px;line-height:1.35}
.tile{position:absolute;width:40px;height:22px;background:#fff;box-shadow:0 1px 4px rgba(0,0,0,.15);display:flex;align-items:center;justify-content:center}
.tile i{display:block;width:20px;height:7px;border-radius:2px;background:#c3cbd6}
.tile i.c{width:9px;height:9px;border-radius:50%}
table{border-collapse:collapse;font-size:3.4px;width:100%}
td,th{padding:3px 4px;text-align:left}
.tbl-a th{background:var(--blue);color:#fff;font-weight:600;text-align:center}
.tbl-a td{text-align:center;border-bottom:1px solid #eee}
.tbl-a tr.band td{background:var(--blue);color:#fff}
.tbl-b th{background:var(--navy);color:#fff;font-weight:600}
.tbl-b td{border-bottom:1px solid #e6e6e6}
.contact{position:absolute;left:44px;list-style:none;font-size:4.2px}
.contact li{display:flex;align-items:center;gap:5px;margin-bottom:7px}
.contact b{background:var(--blue);color:#fff;font-weight:400;padding:1px 5px}
.social{position:absolute;left:232px;list-style:none;font-size:4.2px;color:#555}
.social li{display:flex;align-items:center;gap:6px;margin-bottom:8px}
.social li::before{content:"";width:6px;height:6px;border-radius:50%;background:var(--navy)}
</style>
</head>
<body>
<svg width="0" height="0" style="position:absolute" aria-hidden="true">
  <symbol id="phone" viewBox="0 0 10 10"><path d="M2 0.5 L4 0.5 L4.5 3 L3.3 4 Q4.5 6.2 6 6.7 L7 5.5 L9.5 6 L9.5 8 Q9 9.5 7.5 9.5 Q1 8.5 0.5 2.5 Q0.5 0.5 2 0.5Z"/></symbol>
  <symbol id="pin" viewBox="0 0 10 10"><path d="M5 0.5 A3.5 3.5 0 0 1 8.5 4 C8.5 6.5 5 9.5 5 9.5 C5 9.5 1.5 6.5 1.5 4 A3.5 3.5 0 0 1 5 0.5Z M5 2.5 A1.5 1.5 0 1 0 5 5.5 A1.5 1.5 0 1 0 5 2.5Z" fill-rule="evenodd"/></symbol>
  <symbol id="globe" viewBox="0 0 10 10"><path d="M5 .5a4.5 4.5 0 1 0 0 9a4.5 4.5 0 1 0 0-9Zm0 1a3.5 3.5 0 0 1 0 7a3.5 3.5 0 0 1 0-7ZM1 4.5h8v1H1ZM4.5 1h1v8h-1Z" fill-rule="evenodd"/></symbol>
  <symbol id="mail" viewBox="0 0 10 10"><path d="M.5 2h9v6h-9Zm1 1 3.5 2.5L8.5 3Z" fill-rule="evenodd"/></symbol>
  <symbol id="tick" viewBox="0 0 10 10"><circle cx="5" cy="5" r="4.6"/><path d="M2.8 5.2 4.4 6.7 7.3 3.5" stroke="#fff" stroke-width="1.2" fill="none"/></symbol>
</svg>

<header class="hero">
  <div class="hero-photo" role="img" aria-label="Photo of a crowd raising their hands at sunset"></div>
  <div class="hero-fade"></div>
  <div class="brand">Corvalix</div>
  <h1 class="deck-title"><span class="a">Presentation</span><span class="b">Deck</span></h1>

  <div class="hero-slide slide" style="font-size:468px">
    <div class="title-top photo" role="img" aria-label="Photo of a team working together at laptops"></div>
    <div class="title-main"><strong>PRESENTATION TITLE</strong><em>SUB TITLE GOES HERE</em></div>
    <div class="title-logo logo" style="top:79%;font-size:20px">Corvalix</div>
    <div class="title-foot" style="bottom:8px;font-size:5.5px">
      <span><svg class="ic" style="width:8px;height:8px"><use href="#phone"/></svg>802-431-7296</span>
      <span><svg class="ic" style="width:8px;height:8px"><use href="#pin"/></svg>342 Pebble Creek Road, Ashford Falls, VT 05677</span>
      <span><svg class="ic" style="width:8px;height:8px"><use href="#globe"/></svg>www.Corvalix.com</span>
    </div>
  </div>

  <div class="section-rule"></div>
  <h2 class="section-title">Powerpoint Presentation</h2>
</header>

<main class="grid">
  <section class="slide" style="font-size:353px">
    <div class="title-top photo" role="img" aria-label="Photo of a team working together at laptops"></div>
    <div class="title-main" style="top:30%"><strong>PRESENTATION TITLE</strong><em>SUB TITLE GOES HERE</em></div>
    <div class="title-logo logo" style="top:76%;font-size:13px">Corvalix</div>
    <div class="title-foot" style="bottom:4px;font-size:4px">
      <span><svg class="ic"><use href="#phone"/></svg>802-431-7296</span>
      <span><svg class="ic"><use href="#pin"/></svg>342 Pebble Creek Road, Ashford Falls, VT 05677</span>
      <span><svg class="ic"><use href="#globe"/></svg>www.Corvalix.com</span>
    </div>
  </section>

  <section class="slide swoosh">
    <div class="photo-soft" style="inset:0" role="img" aria-label="Faded photo of colleagues in a meeting"></div>
    <div class="abs" style="left:0;right:0;bottom:0;height:30px;background:var(--navy);clip-path:polygon(0 22px,25% 20px,55% 16px,80% 10px,100% 0,100% 100%,0 100%)"></div>
    <div class="abs" style="left:0;right:0;bottom:0;height:34px;background:var(--orange);clip-path:polygon(0 24px,25% 21px,55% 17px,80% 11px,100% 0,100% 3px,80% 14px,55% 20px,25% 24px,0 26px)"></div>
    <div class="abs logo" style="left:0;right:0;top:32px;text-align:center;font-size:11px">Corvalix</div>
    <div class="abs h" style="left:0;right:0;top:86px;font-size:14px">PRESENTATION TITLE</div>
    <div class="abs sub" style="left:0;right:0;top:105px;letter-spacing:.5px">SUB TITLE GOES HERE</div>
    <div class="abs" style="left:0;right:0;top:138px;text-align:center"><span class="pill">PRESENTER NAME</span></div>
    <div class="title-foot" style="top:166px;font-size:3.8px">
      <span><svg class="ic"><use href="#phone"/></svg>802-431-7296</span>
      <span><svg class="ic"><use href="#pin"/></svg>342 Pebble Creek Road, Ashford Falls, VT 05677</span>
      <span><svg class="ic"><use href="#globe"/></svg>www.Corvalix.com</span>
    </div>
  </section>

  <section class="slide swoosh">
    <div class="abs h" style="left:56px;top:86px;font-size:17px">Agenda</div>
    <ol class="agenda-list">
      <li><i>i.</i>Introduction</li><li><i>ii.</i>About Us</li><li><i>iii.</i>Welcome Message</li><li><i>iv.</i>Company Profile</li><li><i>v.</i>Team</li><li><i>vi.</i>Team Group</li><li><i>vii.</i>Portfolio</li><li><i>viii.</i>Info graphic</li><li><i>ix.</i>Contact Us</li><li><i>x.</i>Data Chart</li>
    </ol>
    <div class="foot"><span class="flogo">Corvalix</span><span><svg class="ic"><use href="#phone"/></svg>802-431-7296</span><span><svg class="ic"><use href="#pin"/></svg>342 Pebble Creek Road, Ashford Falls, VT 05677</span><span><svg class="ic"><use href="#globe"/></svg>www.Corvalix.com</span><b class="pg">3</b></div>
  </section>

  <section class="slide swoosh">
    <div class="abs h" style="left:62px;right:62px;top:70px;font-size:14.5px;line-height:1.45">IT Services That Enable Your Vermont Company To Thrive</div>
    <div class="abs sub" style="left:60px;right:60px;top:118px;letter-spacing:1.2px;font-size:4px">Corvalix Computer Services handles the demands of maintaining your IT infrastructure</div>
    <div class="foot"><span class="flogo">Corvalix</span><span><svg class="ic"><use href="#phone"/></svg>802-431-7296</span><span><svg class="ic"><use href="#pin"/></svg>342 Pebble Creek Road, Ashford Falls, VT 05677</span><span><svg class="ic"><use href="#globe"/></svg>www.Corvalix.com</span><b class="pg">4</b></div>
  </section>

  <section class="slide">
    <div class="photo-soft" style="inset:0 0 14px 0;background:linear-gradient(180deg,#c9d1db,#f3f5f8 70%)" role="img" aria-label="Faded photo of colleagues smiling at a desk"></div>
    <div class="abs logo" style="left:24px;top:36px;font-size:8px">Corvalix</div>
    <div class="abs h" style="left:24px;top:58px;font-size:11px;text-align:left">Your Text Here</div>
    <div class="abs txt" style="left:24px;top:80px;width:140px"><b>Lorem ipsum dolor sit amet.</b> Consectetur adipiscing elit, sed do eiusmod tempor incididunt ut labore et dolore magna aliqua. Ut enim ad minim veniam, quis nostrud exercitation ullamco laboris nisi ut aliquip ex ea commodo consequat. Duis aute irure dolor in reprehenderit in voluptate velit esse cillum dolore eu fugiat nulla pariatur sint occaecat.</div>
    <div class="abs txt" style="left:188px;top:80px;width:140px"><b>Maecenas in purus et tellus tincidunt.</b> Aenean justo diam, commodo vel felis ac, malesuada sodales purus. Nunc sollicitudin sed justo in eleifend. Fusce dictum ornare ligula, eu porttitor elit ullamcorper non. Aliquam erat volutpat. Morbi dui turpis, mollis a ultrices blandit, commodo a enim. Mauris sit amet eleifend sapien.</div>
    <div class="foot"><span class="flogo">Corvalix</span><span><svg class="ic"><use href="#phone"/></svg>802-431-7296</span><span><svg class="ic"><use href="#pin"/></svg>342 Pebble Creek Road, Ashford Falls, VT 05677</span><span><svg class="ic"><use href="#globe"/></svg>www.Corvalix.com</span><b class="pg">5</b></div>
  </section>

  <section class="slide swoosh">
    <div class="abs h" style="left:0;right:0;top:24px;font-size:14px">Overview</div>
    <div class="abs sub" style="left:0;right:0;top:44px">Sub title goes here</div>
    <div class="abs txt" style="left:28px;top:64px;width:140px">Lorem ipsum dolor sit amet, consectetur adipiscing elit, sed do eiusmod tempor incididunt ut labore et dolore magna aliqua. Lorem ipsum dolor sit amet, consectetur adipiscing elit, sed do eiusmod tempor incididunt ut labore et dolore magna aliqua. Ut enim ad minim veniam, quis nostrud exercitation ullamco laboris nisi ut aliquip.<br><br>Lorem ipsum dolor sit amet, consectetur adipiscing elit, sed do eiusmod tempor incididunt ut labore et dolore magna aliqua. Lorem ipsum dolor sit amet, consectetur adipiscing elit, sed do eiusmod tempor incididunt.</div>
    <div class="abs txt" style="left:188px;top:64px;width:140px">Lorem ipsum dolor sit amet, consectetur adipiscing elit, sed do eiusmod tempor incididunt ut labore et dolore magna aliqua. Lorem ipsum dolor sit amet, consectetur adipiscing elit, sed do eiusmod tempor incididunt ut labore.<br><br>Ut enim ad minim veniam, quis nostrud exercitation ullamco laboris nisi ut aliquip. Lorem ipsum dolor sit amet, sed do eiusmod tempor incididunt ut labore et dolore magna aliqua. Lorem ipsum dolor sit amet, consectetur adipiscing elit, sed do eiusmod tempor incididunt.</div>
    <div class="foot"><span class="flogo">Corvalix</span><span><svg class="ic"><use href="#phone"/></svg>802-431-7296</span><span><svg class="ic"><use href="#pin"/></svg>342 Pebble Creek Road, Ashford Falls, VT 05677</span><span><svg class="ic"><use href="#globe"/></svg>www.Corvalix.com</span><b class="pg">6</b></div>
  </section>

  <section class="slide">
    <div class="photo-soft" style="inset:0;background:linear-gradient(135deg,#cfd6df,#eef1f4)" role="img" aria-label="Faded photo of a modern office building"></div>
    <div class="abs" style="left:0;top:32px;width:240px;height:134px;background:var(--blue);border-radius:0 70px 70px 0;box-shadow:0 3px 8px rgba(0,0,0,.25)"></div>
    <div class="abs" style="left:234px;top:84px;width:8px;height:24px;background:var(--orange);border-radius:4px"></div>
    <div class="abs" style="left:14px;top:76px;color:#fff;width:196px">
      <div style="font-size:5px">We Believe Companies Should Be</div>
      <div style="font-size:9px;font-weight:700;line-height:1.1">ACCELERATED BY THEIR IT</div>
      <div style="font-size:11px;font-weight:700;color:var(--orange);line-height:1.1">Not Overwhelmed By It</div>
      <div style="font-size:3.5px;letter-spacing:1px;margin-top:3px;width:180px">WITH NEARLY 20 YEARS OF EXPERIENCE, CORVALIX HAS BEEN SPECIALIZING IN:</div>
    </div>
    <div class="svc" style="top:8px"><i></i>Fixed-Fee Services</div>
    <div class="svc" style="top:52px"><i></i>Business Continuity Planning</div>
    <div class="svc" style="top:96px"><i></i>Consulting</div>
    <div class="svc" style="top:140px"><i></i>Office Suite</div>
  </section>

  <section class="slide swoosh">
    <div class="abs h" style="left:0;right:0;top:32px;font-size:13px">Let Us Handle The Heavy Lifting For You</div>
    <div class="abs sub" style="left:0;right:0;top:50px">Sub title goes here</div>
    <div class="abs" style="left:0;right:0;top:94px;height:64px;background:var(--blue)"></div>
    <div class="numc" style="left:70px;top:78px">01</div>
    <div class="numc" style="left:168px;top:78px">02</div>
    <div class="numc" style="left:272px;top:78px">03</div>
    <div class="card" style="left:34px;top:108px;width:84px;height:34px"><b>WE ANALYZE</b><small>your company and selection</small></div>
    <div class="card" style="left:135px;top:108px;width:84px;height:34px"><b>WE IMPLEMENT</b><small>customized IT solutions</small></div>
    <div class="card" style="left:236px;top:108px;width:84px;height:34px"><b>YOU THRIVE</b><small>on a strong foundation of technology</small></div>
    <div class="foot"><span class="flogo">Corvalix</span><span><svg class="ic"><use href="#phone"/></svg>802-431-7296</span><span><svg class="ic"><use href="#pin"/></svg>342 Pebble Creek Road, Ashford Falls, VT 05677</span><span><svg class="ic"><use href="#globe"/></svg>www.Corvalix.com</span><b class="pg">8</b></div>
  </section>

  <section class="slide">
    <div class="abs h" style="left:28px;top:84px;font-size:15px">Industries</div>
    <div class="abs sub" style="left:18px;top:104px">Sub title goes here</div>
    <div class="ind" style="left:152px;top:40px">Government</div>
    <div class="ind" style="left:245px;top:40px">Professional<br>Services</div>
    <div class="ind" style="left:152px;top:112px">Government</div>
    <div class="ind" style="left:245px;top:112px">Manufacturing</div>
    <div class="foot"><span class="flogo">Corvalix</span><span><svg class="ic"><use href="#phone"/></svg>802-431-7296</span><span><svg class="ic"><use href="#pin"/></svg>342 Pebble Creek Road, Ashford Falls, VT 05677</span><span><svg class="ic"><use href="#globe"/></svg>www.Corvalix.com</span><b class="pg">9</b></div>
  </section>

  <section class="slide">
    <div class="photo" style="left:10px;top:14px;width:158px;height:160px;background:linear-gradient(180deg,#d9e1ea,#a9b7c4 60%,#7f9a6f)" role="img" aria-label="Photo of a domed state capitol building"></div>
    <div class="abs" style="left:16px;top:14px;width:66px;height:86px;background:var(--navy);color:#fff;padding:6px 5px;font-size:3.6px">
      <b>YOUR CONTENT</b> <span style="font-size:10px;opacity:.4">01</span><br>Lorem ipsum dolor sit amet, consectetur adipiscing elit<br><br>
      <b>YOUR CONTENT</b> <span style="font-size:10px;opacity:.4">02</span><br>Lorem ipsum dolor sit amet, consectetur adipiscing elit
    </div>
    <div class="abs h" style="left:178px;top:22px;font-size:14px;text-align:left">Government</div>
    <div class="abs sub" style="left:178px;top:40px;text-align:left">Sub title goes here</div>
    <div class="abs txt" style="left:178px;top:54px;width:150px">Lorem ipsum dolor sit amet, consectetur adipiscing elit, sed do eiusmod tempor incididunt ut labore et dolore magna aliqua. Lorem ipsum dolor sit amet, consectetur adipiscing elit, sed do eiusmod tempor incididunt ut labore et dolore magna aliqua.</div>
    <ul class="bul abs" style="left:178px;top:104px;line-height:1.9">
      <li>Contingency plans</li><li>Communications strategies</li><li>Workflow solutions</li><li>IT staffing services</li><li>Modeling and simulation</li><li>Technologies</li>
    </ul>
    <div class="foot"><span class="flogo">Corvalix</span><span><svg class="ic"><use href="#phone"/></svg>802-431-7296</span><span><svg class="ic"><use href="#pin"/></svg>342 Pebble Creek Road, Ashford Falls, VT 05677</span><span><svg class="ic"><use href="#globe"/></svg>www.Corvalix.com</span><b class="pg">10</b></div>
  </section>

  <section class="slide">
    <div class="photo" style="left:18px;top:18px;width:114px;height:152px;background:linear-gradient(135deg,#8ea5bd,#c9a66a 50%,#4f6e93)" role="img" aria-label="Photo of a smiling professional at an office desk"></div>
    <div class="abs" style="left:92px;top:28px;width:246px;height:34px;background:var(--blue);color:#fff;padding:5px 8px;box-shadow:0 2px 5px rgba(0,0,0,.25)">Lorem ipsum dolor sit amet, consectetur adipiscing elit, sed do eiusmod tempor incididunt ut labore et dolore magna aliqua. Lorem ipsum dolor sit amet, consectetur adipiscing elit, sed do eiusmod tempor.</div>
    <svg class="abs" style="left:142px;top:82px;width:12px;height:12px;fill:var(--navy)"><use href="#tick"/></svg>
    <div class="abs txt" style="left:162px;top:78px;width:172px">Lorem ipsum dolor sit amet, consectetur adipiscing elit, sed do eiusmod tempor incididunt ut labore et dolore magna aliqua. Lorem ipsum dolor sit amet, consectetur adipiscing elit, sed do eiusmod tempor.</div>
    <svg class="abs" style="left:142px;top:132px;width:12px;height:12px;fill:var(--navy)"><use href="#tick"/></svg>
    <div class="abs txt" style="left:162px;top:128px;width:172px">Lorem ipsum dolor sit amet, consectetur adipiscing elit, sed do eiusmod tempor incididunt ut labore et dolore magna aliqua. Lorem ipsum dolor sit amet, consectetur adipiscing elit, sed do eiusmod tempor.</div>
    <div class="foot"><span class="flogo">Corvalix</span><span><svg class="ic"><use href="#phone"/></svg>802-431-7296</span><span><svg class="ic"><use href="#pin"/></svg>342 Pebble Creek Road, Ashford Falls, VT 05677</span><span><svg class="ic"><use href="#globe"/></svg>www.Corvalix.com</span><b class="pg">11</b></div>
  </section>

  <section class="slide">
    <div class="abs h" style="left:0;right:0;top:18px;font-size:13px">Three Important Points</div>
    <div class="abs sub" style="left:0;right:0;top:36px">Sub title goes here</div>
    <svg class="abs" style="left:38px;top:54px;width:120px;height:120px" viewBox="0 0 120 120">
      <g transform="rotate(-90 60 60)" fill="none" stroke-width="22">
        <circle cx="60" cy="60" r="38" stroke="var(--navy)" stroke-dasharray="74 165" stroke-dashoffset="-2"/>
        <circle cx="60" cy="60" r="38" stroke="var(--orange)" stroke-dasharray="74 165" stroke-dashoffset="-82"/>
        <circle cx="60" cy="60" r="38" stroke="#6f93b8" stroke-dasharray="74 165" stroke-dashoffset="-162"/>
      </g>
    </svg>
    <div class="dot" style="left:188px;top:62px;background:var(--navy)"></div>
    <div class="abs txt" style="left:212px;top:62px;width:122px">Lorem ipsum dolor sit amet, consectetur adipiscing elit, sed do eiusmod tempor incididunt ut labore et dolore magna aliqua.</div>
    <div class="dot" style="left:188px;top:96px;background:#6f93b8"></div>
    <div class="abs txt" style="left:212px;top:96px;width:122px">Lorem ipsum dolor sit amet, consectetur adipiscing elit, sed do eiusmod tempor incididunt ut labore et dolore magna aliqua.</div>
    <div class="dot" style="left:188px;top:130px;background:var(--orange)"></div>
    <div class="abs txt" style="left:212px;top:130px;width:122px">Lorem ipsum dolor sit amet, consectetur adipiscing elit, sed do eiusmod tempor incididunt ut labore et dolore magna aliqua.</div>
    <div class="foot"><span class="flogo">Corvalix</span><span><svg class="ic"><use href="#phone"/></svg>802-431-7296</span><span><svg class="ic"><use href="#pin"/></svg>342 Pebble Creek Road, Ashford Falls, VT 05677</span><span><svg class="ic"><use href="#globe"/></svg>www.Corvalix.com</span><b class="pg">12</b></div>
  </section>

  <section class="slide swoosh">
    <div class="abs h" style="left:0;top:28px;font-size:13px;width:330px">A Bit Of Statistics</div>
    <div class="abs sub" style="left:0;width:330px;top:46px">Sub title goes here</div>
    <svg class="abs" style="left:12px;top:64px;width:170px;height:108px" viewBox="0 0 170 108" font-size="3.5" fill="#999">
      <g stroke="#eee" stroke-width=".5">
        <line x1="14" y1="6" x2="165" y2="6"/><line x1="14" y1="22" x2="165" y2="22"/><line x1="14" y1="38" x2="165" y2="38"/><line x1="14" y1="54" x2="165" y2="54"/><line x1="14" y1="70" x2="165" y2="70"/><line x1="14" y1="86" x2="165" y2="86"/><line x1="14" y1="98" x2="165" y2="98"/>
      </g>
      <text x="0" y="8">1000</text><text x="0" y="40">600</text><text x="0" y="72">300</text><text x="0" y="100">0</text>
      <text x="24" y="106">1 quar</text><text x="58" y="106">2 quar</text><text x="96" y="106">3 quar</text><text x="134" y="106">4 quar</text>
      <polyline points="24,26 60,84 96,40 138,78" fill="none" stroke="var(--orange)" stroke-width="2"/>
      <polyline points="24,86 60,38 96,78 138,10" fill="none" stroke="var(--navy)" stroke-width="2"/>
      <g fill="var(--orange)"><circle cx="24" cy="26" r="3.5"/><circle cx="60" cy="84" r="3.5"/><circle cx="96" cy="40" r="3.5"/><circle cx="138" cy="78" r="3.5"/></g>
      <g fill="var(--navy)"><circle cx="24" cy="86" r="3.5"/><circle cx="60" cy="38" r="3.5"/><circle cx="96" cy="78" r="3.5"/><circle cx="138" cy="10" r="3.5"/></g>
    </svg>
    <div class="abs txt" style="left:200px;top:70px;width:136px">Lorem ipsum dolor sit amet, consectetur adipiscing elit, sed do eiusmod tempor incididunt ut labore et dolore magna aliqua. Lorem ipsum dolor sit amet, consectetur adipiscing elit, sed do eiusmod tempor incididunt ut labore et dolore magna aliqua. Lorem ipsum dolor sit amet, consectetur adipiscing elit, sed do eiusmod tempor incididunt ut labore et dolore magna aliqua. Lorem ipsum dolor sit amet, consectetur adipiscing elit, sed do eiusmod tempor incididunt ut labore et dolore magna aliqua.</div>
    <div class="foot"><span class="flogo">Corvalix</span><span><svg class="ic"><use href="#phone"/></svg>802-431-7296</span><span><svg class="ic"><use href="#pin"/></svg>342 Pebble Creek Road, Ashford Falls, VT 05677</span><span><svg class="ic"><use href="#globe"/></svg>www.Corvalix.com</span><b class="pg">13</b></div>
  </section>

  <section class="slide swoosh">
    <div class="abs h" style="left:0;right:0;top:30px;font-size:13px">Your Awesome Text Here</div>
    <div class="abs sub" style="left:0;right:0;top:48px">Sub title goes here</div>
    <svg class="abs" style="left:64px;top:70px;width:52px;height:52px" viewBox="0 0 52 52">
      <circle cx="26" cy="26" r="22" fill="#fff" stroke="#eceff3" stroke-width="5"/>
      <circle cx="26" cy="26" r="17" fill="none" stroke="var(--navy)" stroke-width="2.5" stroke-dasharray="53 107" transform="rotate(-90 26 26)"/>
      <text x="26" y="28" font-size="6" text-anchor="middle" fill="var(--navy)" font-weight="700">50%</text>
    </svg>
    <svg class="abs" style="left:220px;top:70px;width:52px;height:52px" viewBox="0 0 52 52">
      <circle cx="26" cy="26" r="22" fill="#fff" stroke="#eceff3" stroke-width="5"/>
      <circle cx="26" cy="26" r="17" fill="none" stroke="var(--orange)" stroke-width="2.5" stroke-dasharray="101 107" transform="rotate(-90 26 26)"/>
      <text x="26" y="28" font-size="6" text-anchor="middle" fill="var(--orange)" font-weight="700">95%</text>
    </svg>
    <div class="abs txt" style="left:48px;top:130px;width:86px;text-align:center">Lorem ipsum dolor sit amet, consectetur adipiscing elit, sed do eiusmod tempor incididunt ut labore et dolore magna aliqua.</div>
    <div class="abs txt" style="left:204px;top:130px;width:86px;text-align:center">Lorem ipsum dolor sit amet, consectetur adipiscing elit, sed do eiusmod tempor incididunt ut labore et dolore magna aliqua.</div>
    <div class="foot"><span class="flogo">Corvalix</span><span><svg class="ic"><use href="#phone"/></svg>802-431-7296</span><span><svg class="ic"><use href="#pin"/></svg>342 Pebble Creek Road, Ashford Falls, VT 05677</span><span><svg class="ic"><use href="#globe"/></svg>www.Corvalix.com</span><b class="pg">14</b></div>
  </section>

  <section class="slide swoosh">
    <div class="abs h" style="left:0;right:0;top:26px;font-size:13px">Timeline</div>
    <div class="abs sub" style="left:0;right:0;top:44px">Sub title goes here</div>
    <svg class="abs" style="left:0;top:60px;width:353px;height:110px" viewBox="0 0 353 110" font-size="3" text-anchor="middle">
      <line x1="0" y1="58" x2="353" y2="58" stroke="var(--navy)" stroke-width="1.2"/>
      <g fill="#fff" stroke-width="2">
        <circle cx="38" cy="58" r="8" stroke="var(--navy)"/><circle cx="84" cy="58" r="8" stroke="var(--orange)"/><circle cx="130" cy="58" r="8" stroke="var(--navy)"/><circle cx="176" cy="58" r="8" stroke="var(--orange)"/><circle cx="222" cy="58" r="8" stroke="var(--navy)"/><circle cx="268" cy="58" r="8" stroke="var(--orange)"/><circle cx="314" cy="58" r="8" stroke="var(--navy)"/>
      </g>
      <g fill="var(--navy)" font-weight="700"><text x="38" y="59">2015</text><text x="84" y="59">2016</text><text x="130" y="59">2017</text><text x="176" y="59">2018</text><text x="222" y="59">2019</text><text x="268" y="59">2020</text><text x="314" y="59">2021</text></g>
      <g fill="#666">
        <text x="38" y="10">Lorem ipsum dolor sit amet,</text><text x="38" y="15">sed do eiusmod tempor</text><text x="38" y="20">incididunt ut labore</text>
        <text x="130" y="10">Lorem ipsum dolor sit amet,</text><text x="130" y="15">sed do eiusmod tempor</text><text x="130" y="20">incididunt ut labore</text>
        <text x="222" y="10">Lorem ipsum dolor sit amet,</text><text x="222" y="15">sed do eiusmod tempor</text><text x="222" y="20">incididunt ut labore</text>
        <text x="314" y="10">Lorem ipsum dolor sit amet,</text><text x="314" y="15">sed do eiusmod tempor</text><text x="314" y="20">incididunt ut labore</text>
        <text x="84" y="86">Lorem ipsum dolor sit amet,</text><text x="84" y="91">sed do eiusmod tempor</text><text x="84" y="96">incididunt ut labore</text>
        <text x="176" y="86">Lorem ipsum dolor sit amet,</text><text x="176" y="91">sed do eiusmod tempor</text><text x="176" y="96">incididunt ut labore</text>
        <text x="268" y="86">Lorem ipsum dolor sit amet,</text><text x="268" y="91">sed do eiusmod tempor</text><text x="268" y="96">incididunt ut labore</text>
      </g>
      <g stroke="#bbb" stroke-width=".5"><line x1="38" y1="24" x2="38" y2="50"/><line x1="130" y1="24" x2="130" y2="50"/><line x1="222" y1="24" x2="222" y2="50"/><line x1="314" y1="24" x2="314" y2="50"/><line x1="84" y1="66" x2="84" y2="80"/><line x1="176" y1="66" x2="176" y2="80"/><line x1="268" y1="66" x2="268" y2="80"/></g>
    </svg>
    <div class="foot"><span class="flogo">Corvalix</span><span><svg class="ic"><use href="#phone"/></svg>802-431-7296</span><span><svg class="ic"><use href="#pin"/></svg>342 Pebble Creek Road, Ashford Falls, VT 05677</span><span><svg class="ic"><use href="#globe"/></svg>www.Corvalix.com</span><b class="pg">15</b></div>
  </section>

  <section class="slide swoosh">
    <div class="abs h" style="left:0;right:0;top:32px;font-size:13px">Your Awesome Text Here</div>
    <div class="abs sub" style="left:0;right:0;top:50px">Sub title goes here</div>
    <div class="chev" style="left:26px;background:var(--navy)"><b>STEP</b><strong>01</strong><p>Lorem ipsum dolor sit amet, consectetur adipiscing elit, sed do tempor incididunt</p></div>
    <div class="chev" style="left:84px;background:#c9ced6;color:#fff"><b>STEP</b><strong>02</strong><p style="color:var(--orange)">Lorem ipsum dolor sit amet, consectetur adipiscing elit, sed do tempor incididunt</p></div>
    <div class="chev" style="left:142px;background:var(--navy)"><b>STEP</b><strong>03</strong><p>Lorem ipsum dolor sit amet, consectetur adipiscing elit, sed do tempor incididunt</p></div>
    <div class="chev" style="left:200px;background:#c9ced6"><b>STEP</b><strong>04</strong><p style="color:var(--orange)">Lorem ipsum dolor sit amet, consectetur adipiscing elit, sed do tempor incididunt</p></div>
    <div class="chev" style="left:258px;background:var(--navy)"><b>STEP</b><strong>05</strong><p>Lorem ipsum dolor sit amet, consectetur adipiscing elit, sed do tempor incididunt</p></div>
    <div class="foot"><span class="flogo">Corvalix</span><span><svg class="ic"><use href="#phone"/></svg>802-431-7296</span><span><svg class="ic"><use href="#pin"/></svg>342 Pebble Creek Road, Ashford Falls, VT 05677</span><span><svg class="ic"><use href="#globe"/></svg>www.Corvalix.com</span><b class="pg">16</b></div>
  </section>

  <section class="slide swoosh">
    <div class="abs h" style="left:0;right:0;top:28px;font-size:13px">Our Sponsors</div>
    <div class="abs sub" style="left:0;right:0;top:46px">Sub title goes here</div>
    <div class="tile" style="left:42px;top:84px"><i></i></div><div class="tile" style="left:89px;top:84px"><i class="c"></i></div><div class="tile" style="left:136px;top:84px"><i class="c"></i></div><div class="tile" style="left:183px;top:84px"><i></i></div><div class="tile" style="left:230px;top:84px"><i class="c"></i></div><div class="tile" style="left:277px;top:84px"><i></i></div>
    <div class="tile" style="left:42px;top:120px"><i class="c"></i></div><div class="tile" style="left:89px;top:120px"><i></i></div><div class="tile" style="left:136px;top:120px"><i></i></div><div class="tile" style="left:183px;top:120px"><i></i></div><div class="tile" style="left:230px;top:120px"><i class="c"></i></div><div class="tile" style="left:277px;top:120px"><i></i></div>
    <div class="foot"><span class="flogo">Corvalix</span><span><svg class="ic"><use href="#phone"/></svg>802-431-7296</span><span><svg class="ic"><use href="#pin"/></svg>342 Pebble Creek Road, Ashford Falls, VT 05677</span><span><svg class="ic"><use href="#globe"/></svg>www.Corvalix.com</span><b class="pg">17</b></div>
  </section>

  <section class="slide">
    <div class="abs h" style="left:0;right:0;top:12px;font-size:13px">Table</div>
    <div class="abs sub" style="left:0;right:0;top:30px">Sub title goes here</div>
    <div class="abs" style="left:20px;right:20px;top:48px">
      <table class="tbl-a">
        <tr><th></th><th>Content</th><th>Content</th><th>Content</th><th>Content</th><th>Content</th></tr>
        <tr><td>Text Here</td><td>Text Here</td><td>Text Here</td><td>Text Here</td><td>Text Here</td><td>Text Here</td></tr>
        <tr><td>Content</td><td>Content</td><td>Content</td><td>Content</td><td>Content</td><td>Content</td></tr>
        <tr><td>Text Here</td><td>Text Here</td><td>Text Here</td><td>Text Here</td><td>Text Here</td><td>Text Here</td></tr>
        <tr><td>Content</td><td>Content</td><td>Content</td><td>Content</td><td>Content</td><td>Content</td></tr>
        <tr class="band"><td>Text Here</td><td>Text Here</td><td>Text Here</td><td>Text Here</td><td>Text Here</td><td>Text Here</td></tr>
      </table>
      <div style="margin-top:10px;background:var(--orange);color:#fff;text-align:center;padding:3px;font-size:3.6px">You can simply impress your audience and add a unique zing</div>
    </div>
    <div class="foot"><span class="flogo">Corvalix</span><span><svg class="ic"><use href="#phone"/></svg>802-431-7296</span><span><svg class="ic"><use href="#pin"/></svg>342 Pebble Creek Road, Ashford Falls, VT 05677</span><span><svg class="ic"><use href="#globe"/></svg>www.Corvalix.com</span><b class="pg">18</b></div>
  </section>

  <section class="slide">
    <div class="abs h" style="left:0;right:0;top:12px;font-size:13px">Table</div>
    <div class="abs sub" style="left:0;right:0;top:30px">Sub title goes here</div>
    <div class="abs" style="left:18px;right:18px;top:48px">
      <table class="tbl-b">
        <tr><th>No</th><th>Example text</th><th>Example text</th><th>Example text</th><th>Example text</th></tr>
        <tr><td>1</td><td>Lorem ipsum dolor sit amet, consectetur<br>adipiscing elit, sed do eiusmod</td><td>100 %</td><td>120 USD</td><td>1M</td></tr>
        <tr><td>2</td><td>Lorem ipsum dolor sit amet, consectetur<br>adipiscing elit, sed do eiusmod</td><td>100 %</td><td>250 USD</td><td>3M</td></tr>
        <tr><td>3</td><td>Lorem ipsum dolor sit amet, consectetur<br>adipiscing elit, sed do eiusmod</td><td>100 %</td><td>225 USD</td><td>5M</td></tr>
        <tr><td>4</td><td>Lorem ipsum dolor sit amet, consectetur<br>adipiscing elit, sed do eiusmod</td><td>100 %</td><td>100 USD</td><td>1M</td></tr>
        <tr><td>5</td><td>Lorem ipsum dolor sit amet, consectetur<br>adipiscing elit, sed do eiusmod</td><td>100 %</td><td>125 USD</td><td>2M</td></tr>
      </table>
    </div>
    <div class="foot"><span class="flogo">Corvalix</span><span><svg class="ic"><use href="#phone"/></svg>802-431-7296</span><span><svg class="ic"><use href="#pin"/></svg>342 Pebble Creek Road, Ashford Falls, VT 05677</span><span><svg class="ic"><use href="#globe"/></svg>www.Corvalix.com</span><b class="pg">19</b></div>
  </section>

  <section class="slide">
    <div class="abs h" style="left:0;right:0;top:12px;font-size:13px">Infographic</div>
    <div class="abs sub" style="left:0;right:0;top:30px">Sub title goes here</div>
    <svg class="abs" style="left:126px;top:44px;width:100px;height:100px" viewBox="0 0 100 100">
      <g transform="rotate(-90 50 50)" fill="none" stroke-width="18">
        <circle cx="50" cy="50" r="36" stroke="var(--orange)" stroke-dasharray="35 191"/>
        <circle cx="50" cy="50" r="36" stroke="var(--navy)" stroke-dasharray="35 191" stroke-dashoffset="-37.7"/>
        <circle cx="50" cy="50" r="36" stroke="var(--orange)" stroke-dasharray="35 191" stroke-dashoffset="-75.4"/>
        <circle cx="50" cy="50" r="36" stroke="var(--navy)" stroke-dasharray="35 191" stroke-dashoffset="-113.1"/>
        <circle cx="50" cy="50" r="36" stroke="var(--orange)" stroke-dasharray="35 191" stroke-dashoffset="-150.8"/>
        <circle cx="50" cy="50" r="36" stroke="var(--navy)" stroke-dasharray="35 191" stroke-dashoffset="-188.5"/>
      </g>
      <text x="50" y="52" font-size="6" text-anchor="middle" fill="var(--blue)" font-family="Signika, sans-serif" font-weight="700">Corvalix</text>
    </svg>
    <div class="abs txt" style="left:58px;top:46px;width:70px;text-align:right"><b style="color:var(--navy)">Lorem ipsum dolor</b><br>Lorem ipsum dolor sit amet, consectetur adipiscing elit</div>
    <div class="abs txt" style="left:30px;top:92px;width:80px;text-align:right"><b style="color:var(--navy)">Lorem ipsum dolor</b><br>Lorem ipsum dolor sit amet, consectetur adipiscing elit</div>
    <div class="abs txt" style="left:58px;top:140px;width:70px;text-align:right"><b style="color:var(--navy)">Lorem ipsum dolor</b><br>Lorem ipsum dolor sit amet, consectetur adipiscing elit</div>
    <div class="abs txt" style="left:226px;top:46px;width:74px"><b style="color:var(--navy)">Lorem ipsum dolor</b><br>Lorem ipsum dolor sit amet, consectetur adipiscing elit</div>
    <div class="abs txt" style="left:242px;top:92px;width:80px"><b style="color:var(--navy)">Lorem ipsum dolor</b><br>Lorem ipsum dolor sit amet, consectetur adipiscing elit</div>
    <div class="abs txt" style="left:226px;top:140px;width:74px"><b style="color:var(--navy)">Lorem ipsum dolor</b><br>Lorem ipsum dolor sit amet, consectetur adipiscing elit</div>
    <div class="foot"><span class="flogo">Corvalix</span><span><svg class="ic"><use href="#phone"/></svg>802-431-7296</span><span><svg class="ic"><use href="#pin"/></svg>342 Pebble Creek Road, Ashford Falls, VT 05677</span><span><svg class="ic"><use href="#globe"/></svg>www.Corvalix.com</span><b class="pg">20</b></div>
  </section>

  <section class="slide swoosh">
    <div class="abs h" style="left:0;right:0;top:26px;font-size:13px">Infographic</div>
    <div class="abs sub" style="left:0;right:0;top:44px">Sub title goes here</div>
    <svg class="abs" style="left:132px;top:58px;width:90px;height:100px" viewBox="0 0 90 100" font-size="3.5" text-anchor="middle" fill="#fff">
      <path d="M20 14 H62 V6 L76 20 L62 34 V26 H20Z" fill="var(--navy)"/>
      <path d="M82 20 V74 H90 L76 88 L62 74 H70 V20Z" fill="#3d6c9c"/>
      <path d="M70 86 H28 V94 L14 80 L28 66 V74 H70Z" fill="var(--navy)"/>
      <path d="M8 80 V26 H0 L14 12 L28 26 H20 V80Z" fill="#3d6c9c"/>
      <text x="44" y="22">Your Text Here</text><text x="48" y="82">Your Text Here</text>
      <text x="45" y="52" fill="var(--blue)" font-family="Signika, sans-serif" font-weight="700" font-size="5">Corvalix</text>
    </svg>
    <div class="abs" style="left:50px;top:62px;width:80px;text-align:right"><i style="color:var(--navy);font-size:5px">Step 01</i><br>Lorem ipsum dolor consectetur dolor</div>
    <div class="abs" style="left:232px;top:62px;width:90px"><i style="color:var(--navy);font-size:5px">Step 01</i><br>Lorem ipsum dolor consectetur dolor</div>
    <div class="abs" style="left:50px;top:140px;width:80px;text-align:right"><i style="color:var(--navy);font-size:5px">Step 03</i><br>Lorem ipsum dolor consectetur dolor</div>
    <div class="abs" style="left:232px;top:140px;width:90px"><i style="color:var(--navy);font-size:5px">Step 04</i><br>Lorem ipsum dolor consectetur dolor</div>
    <div class="foot"><span class="flogo">Corvalix</span><span><svg class="ic"><use href="#phone"/></svg>802-431-7296</span><span><svg class="ic"><use href="#pin"/></svg>342 Pebble Creek Road, Ashford Falls, VT 05677</span><span><svg class="ic"><use href="#globe"/></svg>www.Corvalix.com</span><b class="pg">21</b></div>
  </section>

  <section class="slide last">
    <div class="photo-soft" style="inset:0 0 100px 0;background:linear-gradient(180deg,#cdd5de,#fff)" role="img" aria-label="Faded photo of business people in conversation"></div>
    <div class="abs" style="left:0;right:0;top:48px;text-align:center;font-size:19px;color:var(--navy);font-family:'Signika',sans-serif"><b>THANK</b> YOU</div>
    <ul class="contact" style="top:120px">
      <li><svg class="ic" style="width:7px;height:7px"><use href="#phone"/></svg><b>802-431-7296</b></li>
      <li><svg class="ic" style="width:7px;height:7px"><use href="#globe"/></svg><b>www.Corvalix.com</b></li>
      <li><svg class="ic" style="width:7px;height:7px"><use href="#mail"/></svg><b>info@website.com</b></li>
      <li><svg class="ic" style="width:7px;height:7px"><use href="#pin"/></svg><b>342 Pebble Creek Road, Ashford Falls, VT 05677</b></li>
    </ul>
    <ul class="social" style="top:120px"><li>Name</li><li>Name</li><li>Name</li><li>Name</li></ul>
    <div class="abs" style="right:26px;bottom:8px;font-size:3.5px;color:#999">22</div>
  </section>
</main>
</body>
</html>
```